Design a leading edge business card for an architectural company

We believe that Velistra Design Collective is redefining the architectural industry. With that, we need a leading edge business card for the company that focuses on landscape architecture, design, and construction.

Our clients are businesses and homeowners so we need a clean, simple, and professional-looking logo. But we want something special. Design must be elegant but unexpected.

Color preferences:
- Preferably with black background but not a must
- Text should be light colored
- Overall, don’t use too much colors.

Content:
- Front of card must contain either just the logo or the logo and business name only.
- Back of card will show the other information (name, title, phone number, email, website, location).

Style:
- Maybe embossing, de-bossing, or spot UV
- Layout should be landscape unless you prove us otherwise.

Size: 1050 x 600 pixels (with 1/8th inch bleed: 1125 x 675 pixels)

Attached is the company logo to incorporate in the design.

```html
<!DOCTYPE html>
<html lang="en">
<head>
<meta charset="utf-8">
<title>Velistra Design Collective — Business Card</title>
<link href="https://fonts.googleapis.com/css2?family=Open+Sans:wght@400;600;700&display=swap" rel="stylesheet">
<style>
  :root {
    --stage: #e9ebed;
    --card-black: #050505;
    --card-white: #ffffff;
    --ink-light: #f4f4f4;
    --ink-navy: #2f4d6e;
    --ink-body: #2a2a2a;
    --faint: #d9dbe3;
    --shadow: rgba(0, 0, 0, 0.18);
  }
  * { margin: 0; padding: 0; box-sizing: border-box; }
  html, body {
    width: 1200px;
    height: 900px;
    overflow: hidden;
    background: var(--stage);
    font-family: "Open Sans", Arial, sans-serif;
  }
  .sheet {
    width: 1200px;
    height: 900px;
    display: flex;
    flex-direction: column;
    align-items: center;
    justify-content: center;
    gap: 40px;
  }
  .card {
    position: relative;
    width: 700px;
    height: 400px;
    overflow: hidden;
    box-shadow: 0 8px 22px var(--shadow);
  }

  /* Front */
  .card--front {
    background: var(--card-black);
    display: flex;
    align-items: center;
    justify-content: center;
  }
  .brand {
    display: flex;
    align-items: center;
    gap: 18px;
  }
  .brand__dot {
    width: 22px;
    height: 22px;
    border-radius: 50%;
    background: var(--ink-light);
  }
  .brand__name {
    color: var(--ink-light);
    font-weight: 400;
    font-size: 30px;
    letter-spacing: 0.16em;
    text-transform: uppercase;
  }

  /* Back */
  .card--back { background: var(--card-white); }
  .back__mark {
    position: absolute;
    right: -70px;
    bottom: -40px;
    width: 300px;
    height: 300px;
    border-radius: 50%;
    background: var(--faint);
    opacity: 0.55;
  }
  .back__brand {
    position: absolute;
    top: 56px;
    right: 54px;
    display: flex;
    align-items: center;
    gap: 10px;
  }
  .back__brand .brand__dot {
    width: 14px;
    height: 14px;
    background: var(--ink-navy);
  }
  .back__brand .brand__name {
    color: var(--ink-navy);
    font-size: 17px;
    letter-spacing: 0.12em;
  }
  .contact {
    position: absolute;
    left: 54px;
    bottom: 52px;
    color: var(--ink-body);
    font-size: 15px;
    line-height: 1.5;
  }
  .contact__name {
    color: var(--ink-navy);
    font-weight: 700;
    font-size: 22px;
    line-height: 1.2;
  }
  .contact__title {
    color: var(--ink-navy);
    font-size: 16px;
    margin-bottom: 16px;
  }
  .contact__address { margin-bottom: 8px; }
  .contact__row {
    display: flex;
    align-items: center;
    gap: 9px;
  }
  .contact__icon {
    width: 14px;
    height: 14px;
    flex: none;
  }
</style>
</head>
<body>
<main class="sheet">

  <section class="card card--front" aria-label="Card front">
    <div class="brand">
      <span class="brand__dot"></span>
      <span class="brand__name">Velistra Design Collective</span>
    </div>
  </section>

  <section class="card card--back" aria-label="Card back">
    <div class="back__mark"></div>

    <div class="back__brand">
      <span class="brand__dot"></span>
      <span class="brand__name">Velistra Design Collective</span>
    </div>

    <div class="contact">
      <p class="contact__name">Dorian Vale</p>
      <p class="contact__title">Buyer</p>
      <p class="contact__address">418 Harbor Lane,<br>Brookfield, NY 10482</p>

      <p class="contact__row">
        <svg class="contact__icon" viewBox="0 0 16 16" aria-hidden="true">
          <path d="M4 1h3l1 4-2 1.5a9 9 0 0 0 3.5 3.5L11 8l4 1v3a2 2 0 0 1-2 2A12 12 0 0 1 2 3a2 2 0 0 1 2-2z" fill="var(--ink-navy)"/>
        </svg>
        <span>555-014-2280</span>
      </p>
      <p class="contact__row">
        <svg class="contact__icon" viewBox="0 0 16 16" aria-hidden="true">
          <rect x="1" y="3" width="14" height="10" rx="1.5" fill="var(--ink-navy)"/>
          <path d="M2 4.5l6 4.5 6-4.5" fill="none" stroke="#fff" stroke-width="1.3"/>
        </svg>
        <span>info@velistradesign.com</span>
      </p>
      <p class="contact__row">
        <svg class="contact__icon" viewBox="0 0 16 16" aria-hidden="true">
          <circle cx="8" cy="8" r="6.5" fill="none" stroke="var(--ink-navy)" stroke-width="1.4"/>
          <ellipse cx="8" cy="8" rx="2.8" ry="6.5" fill="none" stroke="var(--ink-navy)" stroke-width="1.2"/>
          <path d="M1.5 8h13M2.5 5h11M2.5 11h11" stroke="var(--ink-navy)" stroke-width="1.1"/>
        </svg>
        <span>www.velistradesign.com</span>
      </p>
    </div>
  </section>

</main>
</body>
</html>
```